Business Card Design Project

I would like to have a project of business card with incorporated attachted logo elements in warm colors like: gold, yellow, brown.
We would like incorporate below information into the design
Name of the Company: Continental Hoop Invitational
Name: Dorian Pelkey
Position: Project Director
e-mail: dorian@hoopinvitational.net
mobile: +65 83147092
website: www.hoopinvitational.net
Address: 47 Marbury Lane, #06-11, Singapore 915274
There is a picture attachted which can be used as a back side of the buisness card - we would like to follow the colors theme on the front card ( with the person contact details) how ever the front card we will prefer with white background but with graphfic elements coming from logo.
Project Deadline Extended
Reason: the project has been launched on 24 of April with deadline by 24 of April by mistakes. Thats why I would like to extend the deadline.
Name: Dorian Pelkey
mobile: +65 83147092

```html
<!DOCTYPE html>
<html lang="en">
<head>
<meta charset="utf-8">
<title>Continental Hoop Invitational – Business Card</title>
<link rel="stylesheet" href="https://fonts.googleapis.com/css2?family=Open+Sans:wght@400;600;700;800&display=swap">
<style>
  :root {
    --page-bg: #e9e6e3;
    --card-white: #ffffff;
    --indigo: #4a2d91;
    --violet: #7a2a97;
    --magenta: #b0238f;
    --purple-deep: #6c2a94;
    --ink: #2a2a2a;
    --grey-dark: #3a3a3a;
    --grey-mid: #8a8a8a;
  }
  * { box-sizing: border-box; margin: 0; padding: 0; }
  html, body {
    width: 1200px; height: 1024px; overflow: hidden;
    background: var(--page-bg);
    font-family: "Open Sans", Arial, sans-serif;
  }
  .canvas {
    position: relative; width: 1200px; height: 1024px;
  }
  .card {
    position: absolute; left: 210px; width: 780px; height: 446px;
    border-radius: 4px; overflow: hidden;
    box-shadow: 0 6px 18px rgba(0,0,0,0.18);
  }
  .card--front { top: 44px; background: var(--card-white); }
  .card--back {
    top: 534px;
    background: linear-gradient(135deg, var(--magenta) 0%, var(--violet) 55%, var(--purple-deep) 100%);
  }
  .front-graphics { position: absolute; inset: 0; width: 100%; height: 100%; }

  .brand {
    position: absolute; top: 42px; right: 48px;
    display: flex; align-items: center; gap: 12px;
  }
  .brand__dot {
    width: 30px; height: 30px; border-radius: 50%; background: var(--magenta);
  }
  .brand__name {
    font-weight: 800; font-size: 22px; line-height: 1.1;
    color: var(--indigo); text-transform: uppercase; max-width: 260px;
  }

  .person { position: absolute; left: 58px; top: 150px; }
  .person__name {
    font-weight: 800; font-size: 27px; color: var(--indigo);
    text-transform: uppercase; letter-spacing: 0.2px;
  }
  .person__role {
    font-size: 22px; color: var(--violet); margin-top: 2px;
  }
  .person__address {
    font-size: 17px; color: var(--ink); line-height: 1.4; margin-top: 14px;
  }
  .contacts {
    position: absolute; left: 58px; top: 318px; list-style: none;
    font-size: 17px; color: var(--ink); line-height: 1.5;
  }
  .contacts li { display: flex; align-items: center; gap: 10px; }
  .contacts svg { width: 14px; height: 14px; flex: none; }

  .back-brand {
    position: absolute; left: 0; right: 0; top: 150px;
    display: flex; flex-direction: column; align-items: center; gap: 16px;
  }
  .back-brand__dot {
    width: 44px; height: 44px; border-radius: 50%; background: #ffffff;
  }
  .back-brand__name {
    font-weight: 800; font-size: 40px; line-height: 1.1; color: #ffffff;
    text-transform: uppercase; text-align: center; max-width: 520px;
  }
  .back-web {
    position: absolute; left: 60px; bottom: 40px;
    font-size: 16px; color: #ffffff;
  }
</style>
</head>
<body>
<main class="canvas">

  <section class="card card--front" aria-label="Business card front">
    <svg class="front-graphics" viewBox="0 0 780 446" aria-hidden="true">
      <defs>
        <linearGradient id="grey-band" x1="0" y1="1" x2="1" y2="0">
          <stop offset="0" stop-color="#1e1e1e"/>
          <stop offset="1" stop-color="#6b6b6b"/>
        </linearGradient>
        <linearGradient id="purple-band" x1="0" y1="1" x2="1" y2="0">
          <stop offset="0" stop-color="#b0238f"/>
          <stop offset="1" stop-color="#7a2a97"/>
        </linearGradient>
      </defs>
      <path d="M150 446 Q 320 382 540 360 L 540 446 Z" fill="url(#grey-band)"/>
      <path d="M300 446 C 480 404, 680 300, 780 166 L 780 446 Z" fill="url(#purple-band)" stroke="#ffffff" stroke-width="8"/>
      <path d="M420 396 C 610 330, 730 240, 780 104 L 780 132 C 734 258, 620 338, 420 396 Z" fill="var(--indigo)"/>
    </svg>

    <div class="brand">
      <span class="brand__dot"></span>
      <span class="brand__name">Continental Hoop Invitational</span>
    </div>

    <div class="person">
      <h1 class="person__name">Dorian Pelkey</h1>
      <p class="person__role">Project Director</p>
      <p class="person__address">47 Marbury Lane, #06-11,<br>Singapore 915274</p>
    </div>

    <ul class="contacts">
      <li>
        <svg viewBox="0 0 14 14"><rect x="3" y="1" width="8" height="12" rx="1.5" fill="none" stroke="var(--magenta)" stroke-width="1.5"/></svg>
        +65 83147092
      </li>
      <li>
        <svg viewBox="0 0 14 14"><rect x="1" y="3" width="12" height="8" fill="var(--violet)"/><path d="M1 3 L7 8 L13 3" fill="none" stroke="#fff" stroke-width="1.2"/></svg>
        dorian@hoopinvitational.net
      </li>
      <li>
        <svg viewBox="0 0 14 14"><circle cx="7" cy="7" r="6" fill="var(--violet)"/><path d="M1 7 H13 M7 1 C4 4,4 10,7 13 M7 1 C10 4,10 10,7 13" fill="none" stroke="#fff" stroke-width="0.9"/></svg>
        www.hoopinvitational.net
      </li>
    </ul>
  </section>

  <section class="card card--back" aria-label="Business card back">
    <div class="back-brand">
      <span class="back-brand__dot"></span>
      <span class="back-brand__name">Continental Hoop Invitational</span>
    </div>
    <p class="back-web">www.hoopinvitational.net</p>
  </section>

</main>
</body>
</html>
```